Business Card Design for company

We want new business cards. We'd like something different-- yet still highly professional. Our tagline is Providing leadership, delivering success. Stock photos are ok, as long as they are relevant and look upscale.

Target Market(s)

Architecture/Business Management Consulting/Engineering Consulting

Contact Information for Business Card

dark gray background with pops of blue might be good, but you tell me. You're the designers. Rounded corners might be nice, but again, you tell me.

Font styles to use
Serif
Sans Serif

Colors
3276b5
5c5c5c
9d9d9d
fbfbfb

Requirements
Nice to have
• Something different, but still very professional.

```html
<!DOCTYPE html>
<html lang="en">
<head>
<meta charset="utf-8">
<title>Halvern Advisory — Business Cards</title>
<link rel="stylesheet" href="https://fonts.googleapis.com/css2?family=Open+Sans:wght@300;400;600&display=swap">
<style>
  :root {
    --blue: #3276b5;
    --blue-deep: #2a65a0;
    --grey: #5c5c5c;
    --grey-light: #9d9d9d;
    --paper: #fbfbfb;
    --stage: #2b2b2b;
  }
  * { box-sizing: border-box; margin: 0; padding: 0; }
  html, body { width: 1200px; height: 900px; overflow: hidden; }
  body {
    background: var(--stage);
    font-family: "Open Sans", Arial, sans-serif;
    position: relative;
  }
  .card {
    position: absolute;
    width: 540px;
    height: 310px;
    border-radius: 24px;
    overflow: hidden;
    background: var(--paper);
    box-shadow: 0 18px 40px rgba(0,0,0,.45);
  }
  .card--front { left: 80px; top: 110px; }
  .card--back { left: 580px; top: 480px; }

  .wordmark {
    position: absolute;
    display: flex;
    align-items: center;
    gap: 10px;
    font-weight: 600;
    color: var(--grey);
    font-size: 26px;
    letter-spacing: .5px;
    white-space: nowrap;
  }
  .wordmark__square { width: 18px; height: 18px; background: var(--blue); flex: none; }

  /* front */
  .card--front .wordmark { left: 50%; top: 98px; transform: translateX(-50%); }
  .front__band {
    position: absolute; left: 0; right: 0; top: 178px; height: 32px;
    background: var(--grey);
    color: var(--paper);
    font-size: 15px;
    display: flex; align-items: center; justify-content: center;
  }
  .front__base {
    position: absolute; left: 0; right: 0; top: 210px; bottom: 0;
    background: linear-gradient(180deg, var(--blue), var(--blue-deep));
  }
  .notch { position: absolute; top: 206px; height: 10px; background: var(--paper); }
  .front__web {
    position: absolute; left: 0; right: 0; top: 248px;
    text-align: center; color: var(--paper);
    font-size: 15px; letter-spacing: 4px;
  }

  /* back */
  .card--back .wordmark {
    left: 0; width: 220px; top: 128px;
    justify-content: center;
    font-size: 22px; line-height: 1.15;
  }
  .wordmark__stack { display: flex; flex-direction: column; }
  .back__panel {
    position: absolute; left: 220px; right: 0; top: 0; bottom: 0;
    background: linear-gradient(180deg, var(--blue), var(--blue-deep));
  }
  .back__name {
    position: absolute; right: 30px; top: 30px; text-align: right; color: var(--paper);
  }
  .back__name-main { font-size: 20px; font-weight: 400; letter-spacing: .5px; }
  .back__name-title { font-size: 14px; font-weight: 300; }
  .contact {
    position: absolute; left: 0; right: 0; top: 130px;
    display: flex; flex-direction: column; gap: 8px;
  }
  .contact__row { display: flex; align-items: center; height: 26px; position: relative; }
  .contact__icon {
    width: 24px; height: 22px; background: var(--paper);
    display: flex; align-items: center; justify-content: center;
  }
  .contact__icon svg { width: 14px; height: 14px; fill: var(--blue); }
  .contact__text {
    flex: 1; height: 26px; margin-left: 6px; background: var(--paper);
    color: var(--grey); font-size: 14px; padding-left: 12px;
    display: flex; align-items: center;
  }
  .contact__row:nth-child(1) { margin-left: 12px; }
  .contact__row:nth-child(2) { margin-left: 28px; }
  .contact__row:nth-child(3) { margin-left: 44px; }
  .contact__row:nth-child(4) { margin-left: 60px; }
</style>
</head>
<body>

<section class="card card--front" aria-label="Card front">
  <div class="wordmark"><span class="wordmark__square"></span>Halvern Advisory</div>
  <div class="front__band">Providing leadership, Delivering success</div>
  <div class="front__base"></div>
  <div class="notch" style="left:40px;width:50px"></div>
  <div class="notch" style="left:130px;width:80px"></div>
  <div class="notch" style="left:260px;width:80px"></div>
  <div class="notch" style="left:390px;width:80px"></div>
  <div class="notch" style="left:505px;width:35px"></div>
  <div class="front__web">www.yourwebsite.com</div>
</section>

<section class="card card--back" aria-label="Card back">
  <div class="wordmark">
    <span class="wordmark__square"></span>
    <span class="wordmark__stack"><span>Halvern</span><span>Advisory</span></span>
  </div>
  <div class="back__panel">
    <div class="back__name">
      <div class="back__name-main">YOUR NAME</div>
      <div class="back__name-title">Job Title</div>
    </div>
    <div class="contact">
      <div class="contact__row">
        <span class="contact__icon"><svg viewBox="0 0 24 24"><path d="M6.6 10.8a15 15 0 0 0 6.6 6.6l2.2-2.2a1 1 0 0 1 1-.25 11.4 11.4 0 0 0 3.6.57 1 1 0 0 1 1 1V20a1 1 0 0 1-1 1A17 17 0 0 1 3 4a1 1 0 0 1 1-1h3.5a1 1 0 0 1 1 1c0 1.250.2 2.450.57 3.57a1 1 0 0 1-.25 1z"/></svg></span>
        <span class="contact__text">000 000 0000</span>
      </div>
      <div class="contact__row">
        <span class="contact__icon"><svg viewBox="0 0 24 24"><path d="M2 5h20v14H2z M4 7v.5l8 5 8-5V7l-8 5z" fill-rule="evenodd"/></svg></span>
        <span class="contact__text">youremail@xyz.com</span>
      </div>
      <div class="contact__row">
        <span class="contact__icon"><svg viewBox="0 0 24 24"><path d="M12 2a10 10 0 1 0 0 20 10 10 0 0 0 0-20zm0 2c1 1.3 1.8 3 2.2 5H9.8c.4-2 1.2-3.7 2.2-5zM4.3 13a8 8 0 0 1 0-2h3.5a17 17 0 0 0 0 2zm.9 2h2.9c.3 1.4.8 2.6 1.4 3.6A8 8 0 0 1 5.2 15zm4.6 0h4.4c-.4 2-1.2 3.7-2.2 5-1-1.3-1.8-3-2.2-5zm.2-2a15 15 0 0 1 0-2h4a15 15 0 0 1 0 2zm4.5 5.6c.6-1 1.1-2.2 1.4-3.6h2.9a8 8 0 0 1-4.3 3.6zM16.2 13a17 17 0 0 0 0-2h3.5a8 8 0 0 1 0 2zm2.6-4h-2.9c-.3-1.4-.8-2.6-1.4-3.6A8 8 0 0 1 18.8 9zM8.1 9H5.2a8 8 0 0 1 4.3-3.6C8.9 6.4 8.4 7.6 8.1 9z"/></svg></span>
        <span class="contact__text">www.yourwebsite.com</span>
      </div>
      <div class="contact__row">
        <span class="contact__icon"><svg viewBox="0 0 24 24"><path d="M12 2a7 7 0 0 0-7 7c0 5.2 7 13 7 13s7-7.8 7-13a7 7 0 0 0-7-7zm0 9.5A2.5 2.5 0 1 1 12 6.5a2.5 2.5 0 0 1 0 5z"/></svg></span>
        <span class="contact__text">your address here</span>
      </div>
    </div>
  </div>
</section>

</body>
</html>
```